Welding and farication business card

Business name Tbm Welding & Fabrication

I need a business card made for my welding and fabrication business that is bold and stands out. My business is both welding repairs on machinery and anything else you can imagine as well as fabricating new products. i have used this service before and was very happy with the out come of my design logo. i think the card should remain fairly simple and classy but also be bold. I think a black card would best be suited to the talk with my logo on it. i feel the back of the card should just have my logo and the front have my logo email, website and phone number and maybe incorporate a facebook and instagram simple if it can be made look good these arnt a necessity.
I have included both my logo and some business card ideas below

Target Market(s)

Farmers, heavy industry, earthmoving, trucking

Industry/Entity Type

Engineering

Contact Information for Business Card

0438517264
dale@tbmweldingandfabrication.com.au
www.tbmweldingandfabrication.com.au

Colors
33a6d7
0255a3

Requirements
Must have
• Dale Hutchins
my phone number 0438517264
my logo
Preferably a black card desgn
Nice to have
• List of what i do,
Sheds and carports
Ute trays
Stockyards
Trailers
Farm equipment
Stockcrates
Gateways and Entrances
Breakdowns
Maintenance
And lots more!

```html
<!DOCTYPE html>
<html lang="en">
<head>
<meta charset="utf-8">
<title>Tbm Welding &amp; Fabrication – Business Card</title>
<link rel="stylesheet" href="https://fonts.googleapis.com/css2?family=Arimo:wght@400;700&family=Oswald:wght@600&display=swap">
<style>
  :root {
    --backdrop: #2b2b2c;
    --card: #1b1d20;
    --band: #4cc6f2;
    --brand-blue: #1f4f9c;
    --accent-blue: #3a6fd0;
    --text-light: #e9ecef;
    --bullet: #4cc6f2;
  }
  * { box-sizing: border-box; margin: 0; padding: 0; }
  html, body {
    width: 1200px; height: 901px; overflow: hidden;
    background: var(--backdrop);
    font-family: "Arimo", Arial, sans-serif;
  }
  .stage {
    position: relative; width: 1200px; height: 901px;
  }
  .card {
    position: absolute; left: 250px; width: 700px; height: 400px;
    background: var(--card);
    box-shadow: 0 8px 24px rgba(0,0,0,.45);
    overflow: hidden;
  }
  .card::after {
    content: ""; position: absolute; left: 0; right: 0; bottom: 0;
    height: 11px; background: var(--band);
  }
  .card--back { top: 33px; }
  .card--front { top: 468px; }

  .brand {
    display: flex; align-items: center; gap: 14px;
    font-family: "Arimo", Arial, sans-serif; font-weight: 700;
    color: var(--brand-blue); white-space: nowrap;
  }
  .brand__dot {
    width: 18px; height: 18px; border-radius: 50%;
    background: var(--brand-blue); flex: none;
  }
  .card--back .brand {
    position: absolute; left: 0; right: 0; top: 170px;
    justify-content: center; font-size: 38px;
  }
  .card--front .brand {
    position: absolute; left: 40px; top: 170px; font-size: 24px;
  }
  .card--front .brand__dot { width: 14px; height: 14px; }

  .divider {
    position: absolute; left: 392px; top: 60px;
    width: 1px; height: 150px; background: var(--brand-blue);
  }
  .contact {
    position: absolute; left: 410px; top: 60px;
    color: var(--text-light);
  }
  .contact__name {
    font-family: "Oswald", "Arial Narrow", sans-serif; font-weight: 600;
    font-size: 30px; letter-spacing: .5px; text-transform: uppercase;
    color: var(--brand-blue); line-height: 1.1; margin-bottom: 14px;
  }
  .contact__line {
    font-size: 14.5px; line-height: 24px;
  }
  .contact__web-domain { color: var(--accent-blue); }

  .services {
    position: absolute; left: 40px; right: 40px; top: 290px;
    color: var(--text-light); font-size: 17.5px; line-height: 28px;
    list-style: none;
  }
  .services__row { display: block; }
  .services__item::before {
    content: "•"; color: var(--bullet); margin: 0 6px 0 4px;
  }
</style>
</head>
<body>
  <main class="stage">
    <section class="card card--back" aria-label="Card back">
      <div class="brand">
        <span class="brand__dot"></span>
        <span class="brand__name">Tbm Welding &amp; Fabrication</span>
      </div>
    </section>

    <section class="card card--front" aria-label="Card front">
      <div class="brand">
        <span class="brand__dot"></span>
        <span class="brand__name">Tbm Welding &amp; Fabrication</span>
      </div>

      <div class="divider"></div>

      <div class="contact">
        <p class="contact__name">Dale Hutchins</p>
        <p class="contact__line">0438517264</p>
        <p class="contact__line">dale@tbmweldingandfabrication.com.au</p>
        <p class="contact__line">www.<span class="contact__web-domain">tbmweldingandfabrication</span>.com.au</p>
      </div>

      <ul class="services">
        <li class="services__row">
          <span class="services__item">Sheds</span>
          <span class="services__item">Ute trays</span>
          <span class="services__item">Cattle and sheep yards</span>
          <span class="services__item">Trailers</span>
          <span class="services__item">Farm equipment</span>
        </li>
        <li class="services__row">
          <span class="services__item">Gateways and Entrances</span>
          <span class="services__item">Breakdowns</span>
          <span class="services__item">Maintenance</span>
          <span class="services__item">And lots more!</span>
        </li>
      </ul>
    </section>
  </main>
</body>
</html>
```